The Horizonfold LLC Asset Classes

I'm looking for for two designs here to go into powerpoint and potentially as a standalone PDF. My company does wealth management.
Graphic Image #1
I break down the investment world into 4 broad categories
-Preservation
-Capital Markets
-Real Estate
-Alternatives
In each broad category, there are subcategories:
Preservation: cash, checking/savings accounts, money market accounts, CD's, and fixed annuities.
Capital Markets: Publicly traded stocks and bonds
Real Estate: single-family residence, retail, industrial, multifamily, and office
Alternatives: private equity, private credit, cryptocurrency, asset-backed loans, tax liens, oil & gas, litigation finance, and royalties
Graphic 2: Please see the bottom f page 1 of the Lanternway Briefings PDF.
Just like in graphic one, you have 4 categories of the Capital Markets and their respective subcategories
Category 1: Domestic Stocks: Subcategories are Large, mid, and small size companies
Category 2: International Stocks: Subcategories are Large, Mid/Small and by region - Developed and Emerging
Category 3: Fixed Income: You have subcategories like corporate, municipal, government, domestic, international
Category 4: Alternatives: The subcategories are metals and real estate
---------------------
I'm looking to create a graphic (either pie chart, or a circle broken into parts or some other clever way to illustrate this) to clearly illustrate both of these universes in a clean, professional, slick manner.
Target Market(s)
Investors
Colors
Designer to choose colors to be used in the design.
Requirements
Must have
- Clean
- professional
- Easy to read
- Creative
- Visually appealling
Nice to have
- I have attached my logo and some marketing materials so you can get a feel of what I am doing. Maybe you can clean this up too!

```html
<!DOCTYPE html>
<html lang="en">
<head>
<meta charset="utf-8">
<title>The Horizonfold LLC – Asset Classes</title>
<link rel="stylesheet" href="https://fonts.googleapis.com/css2?family=Crimson+Text:wght@600;700&family=Lato:wght@400&display=swap">
<style>
  :root {
    --stage: #76747c;
    --paper: #ffffff;
    --navy: #1d5f8e;
    --deep: #0f4d6b;
    --teal: #2596b4;
    --green: #2e8b3e;
    --orange: #d98e25;
    --grey: #9d9d9d;
    --grey-text: #8a8a8a;
    --ink: #333333;
  }
  * { margin: 0; padding: 0; box-sizing: border-box; }
  html, body { width: 1200px; height: 1200px; overflow: hidden; background: var(--stage); }
  .canvas { position: relative; width: 1200px; height: 1200px; }
  .slide {
    position: absolute; left: 172px; width: 856px; height: 481px;
    background: var(--paper);
    box-shadow: 0 6px 18px rgba(0,0,0,0.35);
    overflow: hidden;
  }
  .slide--overview { top: 70px; }
  .slide--markets { top: 630px; }
  .slide svg { display: block; width: 856px; height: 481px; }
  .title { font-family: "Crimson Text", serif; font-weight: 700; font-size: 50px; fill: var(--navy); }
  .brand { font-family: "Crimson Text", serif; font-weight: 700; font-size: 26px; fill: var(--navy); text-anchor: end; }
  .wedge-label { font-family: "Crimson Text", serif; font-weight: 600; font-size: 17px; fill: #fff; text-anchor: middle; letter-spacing: 0.5px; }
  .wedge-label--small { font-size: 11px; }
  .heading { font-family: "Crimson Text", serif; font-weight: 600; font-size: 17px; letter-spacing: 0.4px; }
  .item { font-family: Lato, sans-serif; font-size: 11.5px; fill: var(--ink); }
  .page-num { font-family: Lato, sans-serif; font-size: 9px; fill: #fff; text-anchor: middle; }
</style>
</head>
<body>
<main class="canvas">

  <section class="slide slide--overview">
    <svg viewBox="0 0 963 541" aria-label="Total Asset Allocation">
      <defs>
        <linearGradient id="waveA" x1="0" y1="0" x2="0" y2="1">
          <stop offset="0" stop-color="#0f4d6b"/>
          <stop offset="1" stop-color="#2aa3be"/>
        </linearGradient>
      </defs>
      <text class="title" x="34" y="62">Total Asset Allocation</text>
      <path d="M34,79 C110,70 200,70 276,73" stroke="var(--orange)" stroke-width="4" fill="none" stroke-linecap="round"/>

      <circle cx="656" cy="72" r="14" fill="var(--navy)"/>
      <text class="brand" x="924" y="81">The Horizonfold LLC</text>

      <g fill="none" stroke-width="1">
        <path d="M77,146 H390" stroke="var(--green)"/>
        <path d="M74,281 H315" stroke="var(--deep)"/>
        <path d="M640,213 H890" stroke="var(--orange)"/>
        <path d="M560,435 H737 V338 H890" stroke="var(--grey)"/>
      </g>

      <circle cx="483" cy="284" r="140" fill="var(--teal)"/>
      <path d="M483,284 L384.3,143.1 A172,172 0 0 1 581.7,143.1 Z" fill="var(--green)"/>
      <path d="M483,284 L623.9,185.3 A172,172 0 0 1 623.9,382.7 Z" fill="var(--orange)"/>
      <path d="M483,284 L581.7,424.9 A172,172 0 0 1 384.3,424.9 Z" fill="var(--grey)"/>
      <path d="M483,284 L342.1,382.7 A172,172 0 0 1 342.1,185.3 Z" fill="var(--deep)"/>
      <circle cx="483" cy="284" r="74" fill="#fff"/>
      <circle cx="483" cy="284" r="66" fill="var(--deep)"/>
      <circle cx="483" cy="284" r="58" fill="#fff"/>

      <text class="wedge-label" x="483" y="172">PRESERVATION</text>
      <text class="wedge-label" x="606" y="272">REAL</text>
      <text class="wedge-label" x="606" y="291">ESTATE</text>
      <text class="wedge-label" x="480" y="402">ALTERNATIVES</text>
      <text class="wedge-label" x="363" y="272">CAPITAL</text>
      <text class="wedge-label" x="363" y="291">MARKETS</text>

      <text class="heading" x="77" y="142" fill="var(--green)">PRESERVATION</text>
      <g class="item">
        <circle cx="80" cy="156" r="2.2" fill="var(--green)"/><text x="88" y="160">Cash</text>
        <circle cx="80" cy="170.5" r="2.2" fill="var(--green)"/><text x="88" y="174.5">Checking/savings accounts</text>
        <circle cx="80" cy="185" r="2.2" fill="var(--green)"/><text x="88" y="189">Money market accounts</text>
        <circle cx="80" cy="199.5" r="2.2" fill="var(--green)"/><text x="88" y="203.5">CD’s</text>
        <circle cx="80" cy="214" r="2.2" fill="var(--green)"/><text x="88" y="218">Fixed annuities</text>
      </g>

      <text class="heading" x="74" y="277" fill="var(--deep)">CAPITAL MARKETS</text>
      <g class="item">
        <circle cx="78" cy="291" r="2.2" fill="var(--deep)"/><text x="86" y="295">Publicly traded stocks</text>
        <circle cx="78" cy="305.5" r="2.2" fill="var(--deep)"/><text x="86" y="309.5">Bonds</text>
      </g>

      <text class="heading" x="763" y="210" fill="var(--orange)">REAL ESTATE</text>
      <g class="item">
        <circle cx="767" cy="223" r="2.2" fill="var(--orange)"/><text x="775" y="227">Single-family Residence</text>
        <circle cx="767" cy="237.5" r="2.2" fill="var(--orange)"/><text x="775" y="241.5">Retail</text>
        <circle cx="767" cy="252" r="2.2" fill="var(--orange)"/><text x="775" y="256">Industrial</text>
        <circle cx="767" cy="266.5" r="2.2" fill="var(--orange)"/><text x="775" y="270.5">Multifamily</text>
        <circle cx="767" cy="281" r="2.2" fill="var(--orange)"/><text x="775" y="285">Office</text>
      </g>

      <text class="heading" x="762" y="335" fill="var(--grey-text)">ALTERNATIVES</text>
      <g class="item">
        <circle cx="767" cy="348" r="2.2" fill="var(--grey)"/><text x="775" y="352">Private Equity</text>
        <circle cx="767" cy="362.5" r="2.2" fill="var(--grey)"/><text x="775" y="366.5">Private Credit</text>
        <circle cx="767" cy="377" r="2.2" fill="var(--grey)"/><text x="775" y="381">Cryptocurrency,</text>
        <circle cx="767" cy="391.5" r="2.2" fill="var(--grey)"/><text x="775" y="395.5">Asset-backed Loans</text>
        <circle cx="767" cy="406" r="2.2" fill="var(--grey)"/><text x="775" y="410">Tax Liens</text>
        <circle cx="767" cy="420.5" r="2.2" fill="var(--grey)"/><text x="775" y="424.5">Oil &amp; Gas</text>
        <circle cx="767" cy="435" r="2.2" fill="var(--grey)"/><text x="775" y="439">Litigation Finance</text>
        <circle cx="767" cy="449.5" r="2.2" fill="var(--grey)"/><text x="775" y="453.5">Royalties</text>
      </g>

      <path d="M0,492 C250,455 560,515 963,486 L963,541 L0,541 Z" fill="url(#waveA)"/>
      <circle cx="897" cy="508" r="17" fill="var(--orange)" stroke="#f3c27a" stroke-width="2"/>
      <text class="page-num" x="897" y="511">3</text>
    </svg>
  </section>

  <section class="slide slide--markets">
    <svg viewBox="0 0 963 541" aria-label="Capital Markets">
      <defs>
        <linearGradient id="waveB" x1="0" y1="0" x2="0" y2="1">
          <stop offset="0" stop-color="#0f4d6b"/>
          <stop offset="1" stop-color="#2aa3be"/>
        </linearGradient>
      </defs>
      <text class="title" x="34" y="62">Capital Markets</text>
      <path d="M95,84 C180,77 260,76 338,79" stroke="var(--orange)" stroke-width="4" fill="none" stroke-linecap="round"/>

      <circle cx="656" cy="72" r="14" fill="var(--navy)"/>
      <text class="brand" x="924" y="81">The Horizonfold LLC</text>

      <g fill="none" stroke-width="1">
        <path d="M77,146 H390" stroke="var(--green)"/>
        <path d="M74,281 H315" stroke="var(--deep)"/>
        <path d="M640,213 H890" stroke="var(--orange)"/>
        <path d="M560,435 H737 V338 H890" stroke="var(--grey)"/>
      </g>

      <circle cx="483" cy="284" r="140" fill="var(--teal)"/>
      <path d="M483,284 L384.3,143.1 A172,172 0 0 1 581.7,143.1 Z" fill="var(--green)"/>
      <path d="M483,284 L623.9,185.3 A172,172 0 0 1 623.9,382.7 Z" fill="var(--orange)"/>
      <path d="M483,284 L581.7,424.9 A172,172 0 0 1 384.3,424.9 Z" fill="var(--grey)"/>
      <path d="M483,284 L342.1,382.7 A172,172 0 0 1 342.1,185.3 Z" fill="var(--deep)"/>
      <circle cx="483" cy="284" r="74" fill="#fff"/>
      <circle cx="483" cy="284" r="66" fill="var(--deep)"/>
      <circle cx="483" cy="284" r="58" fill="#fff"/>

      <text class="wedge-label" x="483" y="172">FIXED INCOME</text>
      <text class="wedge-label wedge-label--small" x="607" y="282">ALTERNATIVES</text>
      <text class="wedge-label" x="481" y="402">INTERNATIONAL</text>
      <text class="wedge-label" x="481" y="421">STOCKS</text>
      <text class="wedge-label" x="363" y="272">DOMESTIC</text>
      <text class="wedge-label" x="363" y="291">STOCKS</text>

      <text class="heading" x="77" y="142" fill="var(--green)">FIXED INCOME</text>
      <g class="item">
        <circle cx="80" cy="156" r="2.2" fill="var(--green)"/><text x="88" y="160">Corporate</text>
        <circle cx="80" cy="170.5" r="2.2" fill="var(--green)"/><text x="88" y="174.5">Municipal</text>
        <circle cx="80" cy="185" r="2.2" fill="var(--green)"/><text x="88" y="189">Government</text>
        <circle cx="80" cy="199.5" r="2.2" fill="var(--green)"/><text x="88" y="203.5">Domestic</text>
        <circle cx="80" cy="214" r="2.2" fill="var(--green)"/><text x="88" y="218">International</text>
      </g>

      <text class="heading" x="74" y="277" fill="var(--deep)">DOMESTIC STOCKS</text>
      <g class="item">
        <circle cx="78" cy="291" r="2.2" fill="var(--deep)"/><text x="86" y="295">Large, mid, and small size</text>
        <text x="86" y="309.5">companies</text>
      </g>

      <text class="heading" x="764" y="210" fill="var(--orange)">ALTERNATIVES</text>
      <g class="item">
        <circle cx="767" cy="223" r="2.2" fill="var(--orange)"/><text x="775" y="227">Metals</text>
        <circle cx="767" cy="237.5" r="2.2" fill="var(--orange)"/><text x="775" y="241.5">Real Estate</text>
      </g>

      <text class="heading" x="762" y="314" fill="var(--grey-text)">INTERNATIONAL</text>
      <text class="heading" x="762" y="333" fill="var(--grey-text)">STOCKS</text>
      <g class="item">
        <circle cx="767" cy="348" r="2.2" fill="var(--grey)"/><text x="775" y="352">Large, Mid/Small and by</text>
        <text x="775" y="366.5">region Developed and</text>
        <text x="775" y="381">Emerging</text>
      </g>

      <path d="M0,492 C250,455 560,515 963,486 L963,541 L0,541 Z" fill="url(#waveB)"/>
      <circle cx="897" cy="508" r="17" fill="var(--orange)" stroke="#f3c27a" stroke-width="2"/>
      <text class="page-num" x="897" y="511">3</text>
    </svg>
  </section>

</main>
</body>
</html>
```